Professional Consulting Firm Business Card Design

We need a business card design for a new professional consulting firm that specializes in petroleum, health, and financial consulting. We need a design that is trendy but elegant, and one that would make a vantage 300 executive feel comfortable using our services. I have attached a logo that needs to be used in the design. I have also attached a photo of a card design that I like.

On the card we need a place for employee name, title, email address, fax number, phone number, mailing address, and website address.

Industry/Entity Type

Financial

Contact Information for Business Card

see attached

Font styles to use
Other font styles liked:
• Calibri or your choice

Requirements
Must have
• style
Nice to have
• texture, rounded edges
Should not have
• no solid black cards but black may be used

```html
<!DOCTYPE html>
<html lang="en">
<head>
<meta charset="utf-8">
<title>Ridgeway Consulting – Business Card</title>
<link rel="stylesheet" href="https://fonts.googleapis.com/css2?family=EB+Garamond:wght@400;600&family=Arimo:wght@400&display=swap">
<style>
  :root {
    --backdrop: #e6e7ea;
    --navy: #1d3a6e;
    --navy-deep: #12264d;
    --navy-light: #2c4f8a;
    --ink: #2b2b2b;
    --ink-soft: #444;
    --paper: #fbfbfb;
    --paper-edge: #ececec;
    --white: #ffffff;
  }
  * { box-sizing: border-box; margin: 0; padding: 0; }
  html, body { width: 1200px; height: 873px; overflow: hidden; }
  body {
    background: var(--backdrop);
    font-family: "EB Garamond", Georgia, serif;
    display: flex;
    flex-direction: column;
    align-items: center;
    justify-content: center;
    gap: 46px;
  }
  .card {
    width: 630px;
    height: 360px;
    border-radius: 10px;
    position: relative;
    box-shadow: 0 6px 18px rgba(0,0,0,.15);
    overflow: hidden;
  }

  /* back side */
  .card--back {
    background: linear-gradient(135deg, var(--navy-light) 0%, var(--navy) 45%, var(--navy-deep) 100%);
  }
  .card--back .texture {
    position: absolute; inset: 0;
    background: linear-gradient(160deg, rgba(255,255,255,.05), rgba(0,0,0,.12));
  }
  .card--back .brand {
    position: absolute; left: 0; right: 0; top: 118px;
    display: flex; justify-content: center; align-items: center; gap: 14px;
  }
  .brand-mark {
    width: 16px; height: 16px;
    background: currentColor;
  }
  .brand-name {
    font-size: 42px; font-weight: 400; letter-spacing: 1px; line-height: 1;
  }
  .brand-tagline {
    font-family: "Arimo", Arial, sans-serif;
    font-size: 8.5px; letter-spacing: .6px; text-transform: uppercase;
    text-align: center;
  }
  .card--back .brand { color: var(--white); }
  .card--back .brand-tagline {
    position: absolute; left: 0; right: 0; top: 172px; color: rgba(255,255,255,.8);
  }
  .card--back .website {
    position: absolute; left: 0; right: 0; top: 212px;
    text-align: center; color: var(--white); font-size: 21px;
  }

  /* front side */
  .card--front {
    background: linear-gradient(135deg, var(--white) 0%, var(--paper) 60%, var(--paper-edge) 100%);
  }
  .card--front .brand {
    position: absolute; left: 0; right: 0; top: 52px;
    display: flex; justify-content: center; align-items: center; gap: 14px;
    color: var(--navy);
  }
  .card--front .brand-tagline {
    position: absolute; left: 0; right: 0; top: 104px; color: var(--navy);
  }
  .divider {
    position: absolute; left: 330px; top: 150px; width: 2px; height: 110px;
    background: linear-gradient(to bottom, transparent, var(--navy) 50%, transparent);
  }
  .contact-list {
    position: absolute; left: 76px; top: 188px;
    list-style: none; color: var(--ink); font-size: 18px;
  }
  .contact-list li { display: flex; align-items: center; gap: 12px; height: 27px; }
  .contact-list svg { width: 16px; height: 14px; fill: var(--navy); }
  .person {
    position: absolute; left: 372px; top: 150px;
  }
  .person-name { color: var(--navy); font-size: 20px; font-weight: 600; }
  .person-title { color: var(--ink); font-size: 15.5px; }
  .address {
    position: absolute; left: 372px; top: 222px;
    color: var(--navy); font-size: 17px; line-height: 1.35; font-style: normal;
  }
  .card--front .website {
    position: absolute; left: 0; right: 0; top: 300px;
    text-align: center; color: var(--ink-soft); font-size: 20px;
  }
</style>
</head>
<body>

<section class="card card--back" aria-label="Card back">
  <div class="texture" role="img" aria-label="Faint faceted navy texture"></div>
  <div class="brand">
    <span class="brand-mark"></span>
    <span class="brand-name">Ridgeway Consulting</span>
  </div>
  <p class="brand-tagline">Health, safety, and financial consulting services</p>
  <p class="website">www.marlowpierce.com</p>
</section>

<section class="card card--front" aria-label="Card front">
  <div class="brand">
    <span class="brand-mark"></span>
    <span class="brand-name">Ridgeway Consulting</span>
  </div>
  <p class="brand-tagline">Health, safety, and financial consulting services</p>

  <ul class="contact-list">
    <li>
      <svg viewBox="0 0 16 14" aria-hidden="true"><path d="M1 5c0-2 3-4 7-4s7 2 7 4l-1 1-3-1V4H5v1L2 6zM4 7h8l2 3v3H2v-3z"/></svg>
      <span>412-555-0120</span>
    </li>
    <li>
      <svg viewBox="0 0 16 14" aria-hidden="true"><path d="M4 1h8v3H4zM1 5h14v6h-3v2H4v-2H1zM5 9v3h6V9z"/></svg>
      <span>412-555-0122</span>
    </li>
    <li>
      <svg viewBox="0 0 16 14" aria-hidden="true"><path d="M1 2h14v10H1zM2 3l6 5 6-5v-.2H2z" fill-rule="evenodd"/></svg>
      <span>dan@marlowpierce.com</span>
    </li>
  </ul>

  <div class="divider"></div>

  <div class="person">
    <p class="person-name">Daniel Kessler</p>
    <p class="person-title">Chief Operating Officer</p>
  </div>
  <address class="address">48 Linden Court,<br>Fairhaven, PA 15290</address>

  <p class="website">www.marlowpierce.com</p>
</section>

</body>
</html>
```